Online trading school - Website design

We are building an online trading school (trading of shares, commodities, indices, currencies). The purpose is to teach online traders how to trade successfully. We need to design the homepage of the website and logo (bramwelloq.com will be the domain). The homepage will contain the following elements

- logo
- Sign in and Register links/buttons
- upper menu
- short introduction
- a couple of bullet points 'Why to join our school?'
- sign up form
- text
- bottom menu

Attached is a draft for the designer. The draft is just for an inspiration, the actual structure of the website can be different if the designer thinks so.

The designer is free to choose colors.

School

3 page

```html
<!DOCTYPE html>
<html lang="en">
<head>
<meta charset="utf-8">
<title>Bramwelloq – Online Trading School</title>
<link rel="stylesheet" href="https://fonts.googleapis.com/css2?family=Merriweather:ital,wght@0,300;0,400;0,700;0,900;1,400&display=swap">
<style>
:root{
  --navy:#10204f;
  --navy-deep:#0b1738;
  --yellow:#e9d50d;
  --yellow-soft:#f3e23a;
  --blush:#ece3df;
  --white:#ffffff;
  --ink:#1b1f2e;
  --grey:#5b5f6b;
  --slate:#3a4f78;
}
*{box-sizing:border-box;margin:0;padding:0}
html,body{width:1200px;height:3797px;overflow:hidden}
body{position:relative;background:var(--blush);font-family:"Merriweather",Georgia,serif;color:var(--ink)}
.abs{position:absolute}
.center{left:0;width:1200px;text-align:center}

/* hero */
.hero{left:0;top:0;width:1200px;height:582px;background:linear-gradient(160deg,#4b5a7c 0%,#2f3d60 45%,#1d2a4c 100%);clip-path:polygon(0 0,100% 0,100% 519px,50% 582px,0 519px);z-index:2}
.topbar-social{top:18px;left:112px;display:flex;gap:12px}
.topbar-social span{width:22px;height:22px;border:2px solid #d5d9e4;border-radius:50%}
.auth{top:20px;right:105px;color:#fff;font-size:13px;display:flex;gap:12px}
.auth .sep{border-left:1px solid #fff}
.nav{top:56px;left:88px;width:1026px;height:88px;background:var(--navy);display:flex;align-items:center;justify-content:space-between;padding:0 26px 0 32px}
.brand{display:flex;align-items:center;gap:10px;color:var(--yellow);font-weight:900;font-size:26px;letter-spacing:.5px}
.brand i{width:14px;height:14px;background:var(--yellow);border-radius:50%;display:block}
.menu{display:flex;align-items:center;gap:30px;font-size:12.5px;color:#fff;font-weight:700}
.menu .active{background:var(--yellow);color:var(--navy);padding:10px 16px;border-radius:3px}
.menu .buy{color:var(--yellow)}
.hero h1{top:206px;font-size:52px;font-weight:900;color:#fff;line-height:64px;letter-spacing:.5px}
.hero .rule{top:346px;left:345px;width:510px;height:2px;background:#cfd4df}
.hero .lede{top:366px;color:#fff;font-size:19px}
.btn{display:flex;align-items:center;justify-content:center;font-weight:700;font-size:14px}
.btn-yellow{background:var(--yellow);color:var(--navy)}
.btn-navy{background:var(--navy);color:#fff}
.hero .start{top:440px;left:524px;width:152px;height:42px}

/* intro */
.intro{left:0;top:500px;width:1200px;height:640px;background:var(--blush);overflow:hidden}
.intro .deco{left:0;top:80px;width:1200px;height:360px;background:radial-gradient(ellipse 180px 140px at 130px 180px,#ddd2ce 0,transparent 100%),radial-gradient(ellipse 200px 150px at 1060px 170px,#ddd2ce 0,transparent 100%)}
.vline{left:599px;width:2px;background:#6f6a6a}
.intro h2,.section-title{font-size:38px;font-weight:700;color:var(--navy)}
.intro h2{top:140px}
.intro .quote{top:200px;color:#c9b500;font-style:italic;font-size:16px}
.intro .ital{top:245px;left:380px;width:440px;text-align:center;font-style:italic;font-size:13px;line-height:19px;color:#2a2e3a}
.intro .body{top:328px;left:380px;width:440px;text-align:center;font-size:12px;line-height:18px;color:var(--grey);font-weight:300}
.intro .more{top:427px;left:546px;width:108px;height:38px;font-size:12px}

/* why */
.why{left:0;top:1063px;width:1200px;height:550px;background:var(--yellow);clip-path:polygon(0 0,50% 58px,100% 0,100% 100%,0 100%)}
.why .section-title{top:115px}
.features{top:224px;left:144px;width:912px;display:flex;justify-content:space-between}
.feature{width:150px;text-align:center}
.feature .disc{width:132px;height:132px;border-radius:50%;background:#fff;margin:0 auto;display:flex;align-items:center;justify-content:center;box-shadow:0 6px 14px rgba(80,70,0,.35)}
.feature p{margin-top:62px;font-size:18px;line-height:22px;color:var(--navy)}

/* offer */
.offer{left:0;top:1613px;width:1200px;height:742px;background:linear-gradient(135deg,#34507f 0%,#243d6c 50%,#162a55 100%)}
.offer .section-title{top:70px;color:var(--yellow);font-size:34px}
.card{top:172px;width:260px;height:473px}
.card-photo{background:linear-gradient(180deg,#a3a8b6 0%,#7c86a0 100%)}
.card-photo .label{position:absolute;left:0;bottom:170px;width:100%;text-align:center;color:#fff;font-weight:700;font-size:15px;line-height:19px}
.card-photo svg{position:absolute;left:100px;top:170px}
.card-main{background:var(--yellow);text-align:center;padding:50px 30px 0}
.card-main h3{font-size:15px;color:var(--navy);margin-top:14px}
.card-main p{font-size:11.5px;line-height:16px;color:var(--navy);margin-top:26px}
.card-main .btn{position:absolute;left:80px;top:400px;width:100px;height:36px;font-size:11px}

/* join */
.join{left:0;top:2355px;width:1200px;height:510px;background:var(--yellow)}
.join .frame{left:84px;top:81px;width:478px;height:387px;border:8px solid var(--navy-deep)}
.join .photo{left:100px;top:100px;width:460px;height:360px;background:linear-gradient(135deg,#f4f6f8 0%,#dfe3ea 60%,#c7ccd6 100%)}
.join h2{left:630px;top:150px;font-size:38px;font-weight:400;color:var(--navy)}
.field{height:40px;border:3px solid var(--navy);background:var(--yellow-soft);font-size:13px;color:var(--navy);padding:9px 10px}
.check{left:630px;top:354px;display:flex;align-items:center;gap:10px;font-size:12px;color:var(--navy)}
.check span{width:18px;height:18px;border:2px solid var(--navy)}
.join .submit{left:1018px;top:402px;width:96px;height:38px;font-size:12px}

/* testimonials */
.testi{left:0;top:2812px;width:1200px;height:710px;background:#fff;clip-path:polygon(0 50px,50% 0,100% 50px,100% 100%,0 100%)}
.testi .city{left:0;top:200px;width:1200px;height:510px;background:linear-gradient(180deg,#fff 0%,#e8ebf2 60%,#dde1ea 100%)}
.testi .section-title{top:152px;font-weight:400}
.avatar{left:567px;top:228px;width:66px;height:66px;border-radius:50%;background:radial-gradient(circle,#d9b39a 0%,#9b7660 100%)}
.qbox{left:172px;top:328px;width:856px;height:101px;background:rgba(160,165,185,.35);padding:26px 30px 0 56px;font-size:13px;line-height:20px;color:#4a4f5e;font-style:italic}
.qmark{left:190px;top:320px;font-size:70px;color:var(--slate);font-weight:900;line-height:70px}
.testi .name{top:474px;font-size:13px;color:var(--navy)}
.testi .role{top:497px;font-size:12px;color:var(--grey)}
.dots{top:537px;left:576px;display:flex;gap:10px}
.dots i{width:9px;height:9px;border-radius:50%;background:var(--yellow)}
.dots i.on{background:var(--navy)}

/* footer */
.footer{left:109px;top:3456px;width:985px;height:266px;background:#fff;box-shadow:0 4px 24px rgba(0,0,0,.12)}
.footer h4{font-size:17px;color:var(--navy);font-weight:700}
.footer .col{position:absolute;top:45px;font-size:12px;line-height:18px;color:var(--grey)}
.footer .col p{margin-top:12px}
.social{display:flex;gap:12px;margin-top:22px}
.social span{width:30px;height:30px;border-radius:50%;background:var(--navy)}
.copy{top:3758px;font-size:11px;color:#333}
</style>
</head>
<body>

<header class="abs hero" role="img" aria-label="Photo of a trader's desk with laptop, charts and glasses, tinted dark blue">
  <div class="abs topbar-social"><span></span><span></span><span></span></div>
  <div class="abs auth"><span>Sign Up</span><span class="sep"></span><span>Register</span></div>
  <nav class="abs nav">
    <div class="brand"><i></i>BRAMWELLOQ</div>
    <div class="menu">
      <span class="active">Home</span><span>Offer and Pricing</span><span>About</span><span>Promotions</span><span>Contact</span><span class="buy">Buy Now</span>
    </div>
  </nav>
  <h1 class="abs center">LEARN HOW TO BE A<br>PROFITABLE TRADER</h1>
  <div class="abs rule"></div>
  <p class="abs center lede">Lorem Ipsum is simply dummy text of the printing.</p>
  <div class="abs btn btn-yellow start">Start Now</div>
</header>

<section class="abs intro">
  <div class="abs deco" role="img" aria-label="Faint bear and bull silhouettes"></div>
  <div class="abs vline" style="top:45px;height:87px"></div>
  <h2 class="abs center">Introduction</h2>
  <p class="abs center quote">"One of the best day trading schools"</p>
  <p class="abs ital">We believe in a world where people manage their own money. That's why we've been building the largest trading school and community for you to get everything you need to succeed.</p>
  <p class="abs body">Learning to trade is a serious topic – at the same time it's fun and much easier when someone shares their knowledge with you and brings you to a level where you can make your own experiences and learn by trading yourself and speaking with others in a community.</p>
  <div class="abs btn btn-yellow more">Read More</div>
  <div class="abs vline" style="top:488px;height:140px"></div>
</section>

<section class="abs why">
  <h2 class="abs center section-title">Why Join Us</h2>
  <div class="abs features">
    <div class="feature"><div class="disc"><svg width="60" height="60" viewBox="0 0 60 60" fill="none" stroke="#10204f" stroke-width="4"><path d="M8 50 L24 32 L34 40 L52 14"/><path d="M40 14 H52 V26"/></svg></div><p>Best trading<br>tips ever.</p></div>
    <div class="feature"><div class="disc"><svg width="60" height="60" viewBox="0 0 60 60" fill="none" stroke="#10204f" stroke-width="4"><circle cx="30" cy="24" r="13"/><path d="M24 40 H36 M25 47 H35"/><path d="M30 4 V1 M12 10 L9 7 M48 10 L51 7"/></svg></div><p>Secret tips<br>from experts.</p></div>
    <div class="feature"><div class="disc"><svg width="60" height="60" viewBox="0 0 60 60" fill="none" stroke="#10204f" stroke-width="4"><rect x="6" y="10" width="48" height="32" rx="2"/><path d="M22 52 H38 M30 42 V52"/><path d="M14 34 L24 24 L32 30 L44 18"/></svg></div><p>We teach you<br>how to trade<br>online.</p></div>
    <div class="feature"><div class="disc"><svg width="60" height="60" viewBox="0 0 60 60" fill="none" stroke="#10204f" stroke-width="4"><path d="M4 10 H12 L18 40 H48 L54 18 H15"/><circle cx="22" cy="50" r="4"/><circle cx="44" cy="50" r="4"/></svg></div><p>Learn how<br>to trade<br>commodities.</p></div>
    <div class="feature"><div class="disc"><svg width="60" height="60" viewBox="0 0 60 60" fill="none" stroke="#10204f" stroke-width="4"><path d="M8 20 H48 M40 12 L48 20 L40 28"/><path d="M52 40 H12 M20 32 L12 40 L20 48"/></svg></div><p>Learn how to<br>become a<br>trader.</p></div>
  </div>
</section>

<section class="abs offer" role="img" aria-label="Photo of hands working over financial charts, tinted blue">
  <h2 class="abs center section-title">What We Offer</h2>
  <div class="abs card card-photo" style="left:190px" role="img" aria-label="Photo of a pen pointing at charts">
    <svg width="60" height="60" viewBox="0 0 60 60" fill="none" stroke="#e9d50d" stroke-width="4"><rect x="6" y="8" width="48" height="36"/><path d="M14 36 L26 24 L34 30 L46 16"/><path d="M22 44 L16 56 M38 44 L44 56"/></svg>
    <div class="label">Largest Site<br>To Learn Trading</div>
  </div>
  <div class="abs card card-main" style="left:468px">
    <svg width="54" height="48" viewBox="0 0 54 48" fill="#10204f"><rect x="10" y="0" width="44" height="30"/><rect x="0" y="16" width="30" height="22" fill="#e9d50d" stroke="#10204f" stroke-width="4"/><rect x="12" y="40" width="30" height="5"/></svg>
    <h3>Best Offers From Brokers</h3>
    <p>More experienced traders who join us find our Intermediate and Advanced sections of the course address a number of techniques that will help reduce your risk and let your profits run. Many traders use our method and techniques as a foundation for other markets to reach profitability.</p>
    <div class="btn btn-navy">Read More</div>
  </div>
  <div class="abs card card-photo" style="left:747px" role="img" aria-label="Photo of colleagues shaking hands">
    <svg width="60" height="60" viewBox="0 0 60 60" fill="#e9d50d"><circle cx="36" cy="18" r="10"/><path d="M18 58 C18 38 54 38 54 58 Z"/><path d="M8 12 H20 M14 6 V18" stroke="#e9d50d" stroke-width="4"/></svg>
    <div class="label">Beginner Friendly<br>Trading Community</div>
  </div>
</section>

<section class="abs join">
  <div class="abs frame"></div>
  <div class="abs photo" role="img" aria-label="Photo of a smiling support agent with headset working at a laptop in front of a rising chart"></div>
  <h2 class="abs">Join our school now!</h2>
  <div class="abs field" style="left:630px;top:243px;width:238px">First Name:</div>
  <div class="abs field" style="left:874px;top:243px;width:240px">Last Name:</div>
  <div class="abs field" style="left:630px;top:299px;width:484px">Email:</div>
  <div class="abs check"><span></span>Agree with our terms &amp; conditions</div>
  <div class="abs btn btn-navy submit">Join Now</div>
</section>

<section class="abs testi">
  <div class="abs city" role="img" aria-label="Faint sketch of a city skyline"></div>
  <h2 class="abs center section-title">Testimonials</h2>
  <div class="abs avatar" role="img" aria-label="Portrait of the reviewer"></div>
  <div class="abs qbox">Contrary to popular belief, Lorem Ipsum is not simply random text. It has roots in a piece of classical Latin literature from 45 BC, making it over 2000 years old.</div>
  <div class="abs qmark">“</div>
  <p class="abs center name">Daniel Hartley</p>
  <p class="abs center role">Graphic Designer</p>
  <div class="abs dots"><i></i><i class="on"></i><i></i></div>
</section>

<footer class="abs footer">
  <div class="col" style="left:35px">
    <h4>Contact us on:</h4>
    <div class="social"><span></span><span></span><span></span></div>
  </div>
  <div class="col" style="left:354px;width:230px">
    <h4>Address:</h4>
    <p>Lorem Ipsum is simply dummy text of the printing and typesetting industry.</p>
    <p>Harbour Court<br>Level 14,Northgate<br>4100 America</p>
  </div>
  <div class="col" style="left:691px;width:240px">
    <h4>Quick Links:</h4>
    <p>Lorem Ipsum is simply dummy text of the printing and typesetting industry.</p>
    <p>Telephone: (05)555-0142</p>
    <p>E-mail: reply@bramwelloq.in</p>
  </div>
</footer>
<p class="abs center copy">Copyright All rights reserved © 2016</p>

</body>
</html>
```